Business Card Design Project

I am community manager and social media strategist. I need a double sided business card with company logo and name. Looking for something professional, elegant but also a little bit original.

• - The logo and the colours are the company colours and a required to stay.
- The size should be: 84 x 55 mm (or 3.30 x 2.16)
- The file size should be: 1039 x 697 pixels (300 dpi)
- I'd like rounded corners. :)

Use the following contact information for the card:

Léonie Vardin
Stratégie médias sociaux / community management / édition de sites sociaux
mob. : 0687529103
leonie.vardin@postelune.fr
Twitter. : @lvardin
Skype : vardin.leonie

```html
<!DOCTYPE html>
<html lang="fr">
<head>
<meta charset="utf-8">
<title>Léonie Vardin – Cartes de visite</title>
<link rel="stylesheet" href="https://fonts.googleapis.com/css2?family=Arimo:wght@400;700&display=swap">
<style>
  :root {
    --page-bg: #d4d4d4;
    --brand-blue: #0b67a5;
    --brand-blue-light: #1a86c9;
    --brand-blue-dark: #07507f;
    --card-grey: #dcdcdc;
    --card-grey-light: #f3f3f3;
    --ink: #111111;
    --muted: #6b6b6b;
    --icon-grey: #8a8a8a;
    --white: #ffffff;
  }
  * { box-sizing: border-box; margin: 0; padding: 0; }
  html, body {
    width: 1200px; height: 805px; overflow: hidden;
    background: var(--page-bg);
    font-family: "Arimo", Arial, sans-serif;
  }
  .sheet {
    width: 1200px; height: 805px;
    display: flex; align-items: center; justify-content: center; gap: 40px;
  }
  .card {
    position: relative;
    width: 540px; height: 354px;
    border-radius: 14px;
    overflow: hidden;
    box-shadow: 0 10px 30px rgba(0,0,0,0.18);
  }

  /* Front side */
  .card-front {
    background: linear-gradient(160deg, var(--brand-blue-light) 0%, var(--brand-blue) 50%, var(--brand-blue-dark) 100%);
  }
  .card-front .swoosh { position: absolute; inset: 0; width: 100%; height: 100%; }
  .brand {
    position: absolute; left: 0; right: 0; top: 120px;
    display: flex; flex-direction: column; align-items: center; gap: 10px;
    color: var(--white);
  }
  .brand-dot {
    width: 38px; height: 38px; border-radius: 50%;
    background: var(--white);
  }
  .brand-name {
    font-weight: 700; font-size: 26px; letter-spacing: 4px;
  }

  /* Back side */
  .card-back {
    background: radial-gradient(ellipse at 40% 45%, var(--card-grey-light) 0%, var(--card-grey) 75%);
    border: 6px solid var(--white);
  }
  .corner-tab {
    position: absolute; top: 0; right: 40px;
    width: 70px; height: 14px; background: var(--white);
  }
  .name-ghost {
    position: absolute; left: 40px; top: 88px;
    font-weight: 700; font-size: 120px; line-height: 1;
    color: rgba(255,255,255,0.55);
    letter-spacing: -2px;
  }
  .identity { position: absolute; left: 40px; top: 150px; }
  .person-name {
    font-weight: 700; font-size: 38px; color: var(--ink); letter-spacing: -0.5px;
  }
  .person-name .surname { color: var(--brand-blue); }
  .role {
    margin-top: 4px; font-size: 12.5px; color: var(--muted);
  }
  .contacts {
    position: absolute; right: 34px; top: 70px;
    list-style: none; font-size: 10px; color: var(--brand-blue);
  }
  .contacts li { display: flex; align-items: center; gap: 7px; margin-bottom: 5px; }
  .contacts .icon {
    width: 11px; height: 11px; border-radius: 50%; background: var(--icon-grey);
    flex: none;
  }
  .accent-bar {
    position: absolute; left: 40px; bottom: 22px;
    width: 230px; height: 16px; background: var(--brand-blue);
  }
</style>
</head>
<body>
<main class="sheet">
  <section class="card card-front" aria-label="Recto">
    <svg class="swoosh" viewBox="0 0 540 354" preserveAspectRatio="none" aria-hidden="true">
      <path d="M0 300 C160 250 330 215 540 160" fill="none" stroke="#ffffff" stroke-width="6"/>
      <path d="M0 330 C170 285 340 250 540 200" fill="none" stroke="#ffffff" stroke-width="3"/>
      <path d="M0 300 C160 250 330 215 540 160 L540 354 L0 354 Z" fill="rgba(0,0,0,0.08)"/>
    </svg>
    <div class="brand">
      <span class="brand-dot"></span>
      <span class="brand-name">VENTARA</span>
    </div>
  </section>

  <section class="card card-back" aria-label="Verso">
    <span class="corner-tab"></span>
    <div class="name-ghost" aria-hidden="true">Léonie</div>
    <div class="identity">
      <h1 class="person-name">Léonie <span class="surname">Vardin</span></h1>
      <p class="role">Stratégie médias sociaux / community management / édition de sites</p>
    </div>
    <ul class="contacts">
      <li><span class="icon"></span>leonie.vardin@postelune.fr</li>
      <li><span class="icon"></span>0687529103</li>
      <li><span class="icon"></span>vardin.leonie</li>
      <li><span class="icon"></span>@lvardin</li>
    </ul>
    <span class="accent-bar"></span>
  </section>
</main>
</body>
</html>
```